Graphical design for food product in 1 Liter carton

We need this design not for a real product but as a showcase for a new service.

This special situation makes it really simple for you to participate because you only have to care about how the visual impression of your design is.

Furthermore it gives you the opportunity to get an extra winning chance if you choose to also participate in the open competition at our website - where you can enter the same design as you enter here at ArtQuarry.

Here is the requirements:

1. You must apply your design to our attatched template

2. Make a design for a food product of your own choice, which is to be sold from retail stores in a rectangular 1 L carton – based on our template.

3. You are only allowed to use brand names and/or logos that you have the rights to use for this competition, so please make completely fictive brand names and logos.

4. Your design is evaluated on the visual impression only, which means that your text on the design can be in any language and doesn’t have to relate to the design.

5. The criteria for the evaluation of your design is your creativity, the graphical quality and how well the product will display it self in the stores.

If you also want to participate in the open competition on our website - where you can win an Zelbo Slate, and will get your design skills exposed to brand owners and packaging manufacturers all over the world, then please visit plovimark.example/packaging-design-competition/

Attatched is:

A. Empty design template you must apply your design to. Remove the layer with our template when you return your send in your design.

B. Example of design applied to the template.

C. Example of the applied example design after it has been converted to 3D with our online 3D engine at PloviMark.example.

The winning design will be converted to 3D and will be used as a showcase on our website - all designers can enter their design to our open competition at PloviMark.example.

```html
<!DOCTYPE html>
<html lang="en">
<head>
<meta charset="utf-8">
<title>Sunpress Orange – 1 L carton</title>
<link rel="stylesheet" href="https://fonts.googleapis.com/css2?family=Montserrat:wght@400;600;800&display=swap">
<style>
  :root {
    --bg: #ffffff;
    --red: #e01519;
    --red-deep: #c80f15;
    --amber: #f2b52a;
    --yellow: #f0e020;
    --lime: #e6ff10;
    --band: #141414;
    --white: #ffffff;
    --orange: #f39a1c;
    --orange-deep: #e2700c;
  }
  * { box-sizing: border-box; margin: 0; padding: 0; }
  html, body { width: 1200px; height: 900px; overflow: hidden; background: var(--bg); }
  body { font-family: "Montserrat", sans-serif; }

  .carton-net {
    position: absolute; left: 290px; top: 80px;
    display: flex; width: 620px; height: 740px;
  }
  .panel { position: relative; width: 310px; height: 740px; overflow: hidden; }

  /* front panel */
  .panel--front {
    background: linear-gradient(180deg, var(--red) 0%, var(--red) 10%, var(--amber) 30%, var(--yellow) 60%, var(--lime) 85%);
  }
  .bubble { position: absolute; border-radius: 50%; background: rgba(255,255,255,0.4); }
  .brand {
    position: absolute; left: 20px; top: 190px; width: 190px; z-index: 3;
    display: flex; flex-direction: column; align-items: center; gap: 10px;
  }
  .brand__dot { width: 54px; height: 54px; border-radius: 50%; background: var(--red-deep); }
  .brand__name { font-weight: 800; font-size: 34px; color: var(--red-deep); letter-spacing: 0.5px; line-height: 1.1; }
  .flavour-band {
    position: absolute; left: 60px; top: 310px; width: 80px; height: 430px; z-index: 2;
    background: linear-gradient(180deg, rgba(20,20,20,0) 0%, var(--band) 10%, var(--band) 100%);
  }
  .flavour-band__label {
    position: absolute; left: 50%; top: 50%;
    transform: translate(-50%, -50%) rotate(-90deg);
    color: var(--white); font-weight: 800; font-size: 54px; line-height: 1; letter-spacing: 1px; white-space: nowrap;
  }
  .fruit-strip {
    position: absolute; left: 0; bottom: 0; width: 100%; height: 100px; z-index: 1;
    background: linear-gradient(180deg, var(--orange) 0%, var(--orange-deep) 100%);
    border-radius: 60% 60% 0 0 / 40% 40% 0 0;
  }

  /* side panel */
  .panel--side { background: var(--red); }
  .fruit-slice {
    position: absolute; left: 170px; top: 170px; width: 190px; height: 190px; border-radius: 50%;
    background: radial-gradient(circle, rgba(243,140,40,0.55) 0%, rgba(230,90,30,0.35) 100%);
  }
  .copy {
    position: absolute; left: 30px; top: 255px; width: 230px; z-index: 2;
    display: flex; flex-direction: column; gap: 14px;
  }
  .copy p { color: var(--white); font-size: 9.5px; line-height: 1.45; font-weight: 400; }
  .brand--small { left: 150px; top: 520px; width: 140px; gap: 6px; }
  .brand--small .brand__dot { width: 34px; height: 34px; background: var(--amber); }
  .brand--small .brand__name { font-size: 24px; color: var(--white); }
</style>
</head>
<body>
  <main class="carton-net">
    <section class="panel panel--front">
      <span class="bubble" style="left:80px;top:60px;width:44px;height:44px"></span>
      <span class="bubble" style="left:15px;top:250px;width:32px;height:32px"></span>
      <span class="bubble" style="left:15px;top:520px;width:30px;height:30px"></span>
      <span class="bubble" style="left:160px;top:540px;width:90px;height:90px"></span>
      <span class="bubble" style="left:150px;top:610px;width:46px;height:46px"></span>

      <div class="brand">
        <span class="brand__dot"></span>
        <span class="brand__name">Sunpress</span>
      </div>

      <div class="flavour-band"><span class="flavour-band__label">ORANGE</span></div>

      <div class="fruit-strip" role="img" aria-label="Halved orange slices along the bottom edge"></div>
    </section>

    <section class="panel panel--side">
      <span class="bubble" style="left:90px;top:65px;width:44px;height:44px;background:rgba(255,255,255,0.35)"></span>
      <span class="bubble" style="left:10px;top:560px;width:120px;height:120px;background:rgba(255,255,255,0.3)"></span>
      <div class="fruit-slice" role="img" aria-label="Faint sliced orange behind the product text"></div>

      <div class="copy">
        <p>Squeezed from ripe sun grown oranges every morning and packed within hours to keep the bright taste of the grove. No added sugar, no colouring, nothing but pure fruit juice in every glass you pour.</p>
        <p>Shake well before serving. Keep refrigerated after opening and enjoy within five days. Best served chilled with breakfast or as a fresh lift at any time of day.</p>
        <p>Ingredients: one hundred percent orange juice. Store in a cool dry place before opening.</p>
      </div>

      <div class="brand brand--small">
        <span class="brand__dot"></span>
        <span class="brand__name">Sunpress</span>
      </div>

      <div class="fruit-strip" role="img" aria-label="Halved orange slices along the bottom edge"></div>
    </section>
  </main>
</body>
</html>
```